A new company focused on starting and investing in transformative businesses.

We need a simple and clean website with a few pages. we like larkmeadow.com as a starting point. we want the landing page to be very simple with an option to click through on the top right into INVESTOR LOGIN. then we want to be able to scroll down to see more about our company.

Target Market(s)

professional

Coding

Coded - Design and coding required

Number of Pages Required

2 page

Font styles to use
Serif
Sans Serif

Requirements
Must have
• HALVERN BUILDERS logo (attached as a file) on the top with INVESTOR LOGIN as a click through on the right. Please model the click through from larkmeadow.com. The description (also written in attached file) should be on the landing page. we do not want to have to scroll to read the description.

Then we can scroll down to read more about Halvern including the mission and the two types of businesses. More is detailed on the attached file called "Halvern Website Syntax"
Should not have
• should not be slow loading with lots of fancy graphics. should not be busy and with too many colors.

```html
<!DOCTYPE html>
<html lang="en">
<head>
<meta charset="utf-8">
<title>Halvern Builders</title>
<link rel="stylesheet" href="https://fonts.googleapis.com/css2?family=Arimo:ital,wght@0,400;0,700;1,400&family=Mulish:wght@400;700&display=swap">
<style>
:root{
  --brand:#0d4fa1;
  --ink:#2b2d33;
  --muted:#3a3d44;
  --hero-a:#f4f4f5;
  --hero-b:#e2e2e4;
  --section:#f2f5f9;
  --card:#ffffff;
  --icon-bg:#e3eefb;
}
*{box-sizing:border-box;margin:0;padding:0}
html,body{width:831px;height:1200px;overflow:hidden;background:#fff}
body{position:relative;font-family:"Arimo",Arial,sans-serif;color:var(--ink)}
.abs{position:absolute}

.hero{left:0;top:0;width:831px;height:442px;background:linear-gradient(125deg,var(--hero-a) 0%,#ececed 45%,var(--hero-b) 100%)}
.brand-name{left:111px;top:29px;font-size:19px;font-weight:700;color:var(--brand);letter-spacing:.5px;line-height:1.15}
.login-btn{left:595px;top:34px;width:125px;height:26px;border-radius:13px;background:var(--brand);color:#fff;font-size:9.5px;font-weight:700;display:flex;align-items:center;justify-content:center;text-decoration:none}
.side-label{left:111px;top:182px;height:129px;border-left:1px solid var(--brand);padding-left:3px;writing-mode:vertical-rl;font-size:9px;font-weight:700;letter-spacing:.4px;color:var(--ink)}
.headline{left:147px;top:178px;width:440px;font-size:25px;line-height:36px;font-weight:400;color:var(--ink)}
.scroll-line{left:111px;top:348px;width:1px;height:31px;background:var(--brand)}
.scroll-dot{left:99px;top:385px;width:24px;height:24px;border-radius:50%;background:#fff}
.scroll-dot svg{position:absolute;left:2px;top:2px}
.scroll-text{left:150px;top:392px;font-size:8.5px;font-style:italic;color:var(--ink)}

.mission{left:111px;top:490px;width:609px;text-align:center;font-family:"Mulish",sans-serif;font-size:15.5px;line-height:23px;color:var(--muted)}
.mission b{font-weight:700;color:var(--ink)}

.card{top:553px;width:288px;height:147px;background:var(--card);border-radius:4px;box-shadow:0 2px 10px rgba(30,40,60,.08)}
.card-ground{left:111px}
.card-special{left:431px}
.card svg{position:absolute;left:12px;top:14px}
.card h3{position:absolute;left:64px;top:19px;font-size:16px;font-weight:400;color:var(--ink)}
.card h3 b{color:var(--brand)}
.card p{position:absolute;left:64px;top:42px;width:202px;font-size:9px;line-height:15px;text-align:justify;color:var(--muted)}

.team{left:0;top:752px;width:831px;height:415px;background:var(--section)}
.team-title{left:0;top:800px;width:831px;text-align:center;font-size:25px;color:var(--ink)}
.team-title b{color:var(--brand)}
.team-intro{left:170px;top:836px;width:491px;text-align:center;font-size:10.5px;line-height:17px;color:var(--muted)}
.member{top:886px;width:135px;text-align:center}
.photo{width:135px;height:181px;border-radius:4px;background:linear-gradient(180deg,#dcdde0,#b9bcc2)}
.name{margin-top:9px;font-size:11.5px;font-weight:700;letter-spacing:.5px;color:var(--muted)}
.role{margin-top:4px;font-size:9.5px;color:var(--brand)}
.member.active{height:229px;border-radius:4px;background:linear-gradient(180deg,#8c8d90 0%,#2a2a2c 70%,#111 100%);overflow:hidden}
.member.active .photo{background:linear-gradient(180deg,#c9c9cb,#5a5a5d 70%,#2a2a2c)}
.member.active .name,.member.active .role{color:#fff;position:relative;top:-18px}
.member.active .name{margin-top:0}

.footer{left:0;top:1167px;width:831px;height:33px;background:var(--brand);color:#fff;font-size:9.5px;display:flex;align-items:center;justify-content:center}
</style>
</head>
<body>
<section class="abs hero"></section>
<div class="abs brand-name">HALVERN<br>BUILDERS</div>
<a class="abs login-btn" href="#">INVESTMENT LOGIN</a>
<div class="abs side-label">FINANCIAL INVESTMENT</div>
<h1 class="abs headline">HALVERN BUILDERS IS AN ENTREPRENEURIAL FIRM FOCUSED ON BUILDING AND GROWING TRANSFORMATIONAL COMPANIES</h1>
<div class="abs scroll-line"></div>
<div class="abs scroll-dot"><svg width="20" height="20" viewBox="0 0 20 20"><circle cx="10" cy="10" r="10" fill="#0d4fa1"/><path d="M10 5v9M6.5 10.5 10 14l3.5-3.5" stroke="#fff" stroke-width="1.3" fill="none"/></svg></div>
<div class="abs scroll-text">SCROLL DOWN</div>

<p class="abs mission">Our mission is to build <b>meaningful</b> businesses that create <b>enduring</b> value by impacting people in a <b>measurable</b> way.</p>

<article class="abs card card-ground">
  <svg width="40" height="38" viewBox="0 0 40 38"><circle cx="13" cy="22" r="12" fill="#e3eefb"/><g stroke="#2b2d33" stroke-width="1" fill="none"><rect x="10" y="25" width="3" height="4"/><rect x="15" y="23" width="3" height="6"/><rect x="20" y="19" width="3" height="10"/><rect x="25" y="14" width="3" height="15"/><path d="M8 31h28M10 21l8-4 6-3 10-9"/></g><path d="M31 4l4 0 0 4" stroke="#0d4fa1" stroke-width="1.2" fill="none"/><path d="M10 6h5M10 8h5M10 10h4" stroke="#0d4fa1"/></svg>
  <h3><b>GROUND</b> UP</h3>
  <p>Our ground up business applies a proven analytic process to identify value edge, a form of competitive advantage. We architect transformational companies and are deliberate in creating the foundation necessary to lead an industry.</p>
</article>
<article class="abs card card-special">
  <svg width="40" height="38" viewBox="0 0 40 38"><circle cx="13" cy="22" r="12" fill="#e3eefb"/><circle cx="27" cy="8" r="5" fill="none" stroke="#0d4fa1"/><path d="M27 5v6M25.5 6.5h2.5a1 1 0 0 1 0 2h-1.5a1 1 0 0 0 0 2H29" stroke="#0d4fa1" stroke-width=".8" fill="none"/><path d="M10 26l6-5h7l-1 3h-5M16 24h8l8-6 2 2-9 8H15l-3 2z" stroke="#2b2d33" fill="none"/></svg>
  <h3><b>SPECIAL</b> OPPORTUNITIES</h3>
  <p>We partner with exceptional teams that create value by transforming lives. Our investment focus includes large companies and spin-outs.</p>
</article>

<section class="abs team"></section>
<h2 class="abs team-title"><b>HALVERN</b> BUILDERS</h2>
<p class="abs team-intro">Lorem ipsum dolor sit amet, consectetuer adipiscing elit, sed diam nonummy nibh euismod tincidunt ut laoreet dolore magna aliquam erat volutpat.</p>

<div class="abs member" style="left:111px"><div class="photo" role="img" aria-label="Portrait photo of Owen Talbot"></div><div class="name">OWEN TALBOT</div><div class="role">Co Founder</div></div>
<div class="abs member active" style="left:269px"><div class="photo" role="img" aria-label="Portrait photo of Clara Whitfield"></div><div class="name">CLARA WHITFIELD</div><div class="role">General Manager</div></div>
<div class="abs member" style="left:426px"><div class="photo" role="img" aria-label="Portrait photo of Peter Lindqvist"></div><div class="name">PETER LINDQVIST</div><div class="role">Senior Designer</div></div>
<div class="abs member" style="left:584px"><div class="photo" role="img" aria-label="Portrait photo of Nora Castell"></div><div class="name">NORA CASTELL</div><div class="role">Marketing Manager</div></div>

<footer class="abs footer">Copyright 2021 Halvern Investment Financial. All Rights Reserved.</footer>
</body>
</html>
```